Business Card Design

I am starting up a clothing business that designs and manufactures clothing for those with a disability in the younger age group of 16-28 years. My disabled daughter has finished school and as her mother I am aware of the difficulties in finding clothing to fit her. I am also aware of the difficulty for others of her age group regardless of gender who have difficulty dressing in clothes that suit their age because of their affliction.

I would like a card that has a design on the front referring to an unlimited sky and perhaps a rainbow or balloons indicating limitless possibilities. Within the rainbow of jewel colours (rather than typical red, yellow etc) I wish to contain words along the lines of ......For the young adult, Wheelchair bound, Restricted movement, Fumble free designs, On trend, Grace and dignity, Unique to your needs.

On the reverse or interior of a folding card I would like ......:-
Design & Manufacture of clothing for those with limited physical or cognitive ability at 47 Tallowmere Road, Wattlebrook, Qld, 4759

Name: …………………………………………………………….………
Your next appointment is ……..../……..../…….... at the time of …………………….. to be held at ……………………….
…………………………………………………………………………………

Target Market(s)

audience of any age, product targets 18-28 years age group with disabilties

Industry/Entity Type

Clothing

Contact Information for Business Card

MARIGOLD HOLLOW CLOTHING – 0417 296 514

PO Box 3126
Mount Pleasant Qld 4740

Requirements
Must have
• reference to a sky with some clouds, a rainbow or hot air balloons or some other item of many colours indicating the sky/possibilities are endless
Should not have
• people of obvious disabilities displayed

```html
<!DOCTYPE html>
<html lang="en">
<head>
<meta charset="utf-8">
<title>Marigold Hollow Clothing – Appointment Card</title>
<link rel="stylesheet" href="https://fonts.googleapis.com/css2?family=Cormorant+Garamond:wght@500&display=swap">
<style>
  :root {
    --panel-lilac: #dcc2df;
    --ink-brown: #7e6650;
    --divider: #ffffff;
    --sky-top: #8cd6fb;
    --sky-mid: #a6f6fb;
    --sky-violet: #caa9f7;
    --sky-orchid: #d6a3ee;
    --sky-blush: #f6abb2;
    --hill-green: #6aa94a;
  }
  html, body {
    margin: 0;
    padding: 0;
    overflow: hidden;
    background: var(--divider);
  }
  .card {
    position: relative;
    width: 1200px;
    height: 900px;
    overflow: hidden;
    background: var(--divider);
    font-family: "Cormorant Garamond", serif;
    font-weight: 500;
    color: var(--ink-brown);
  }
  .panel {
    position: absolute;
    top: 0;
    height: 900px;
  }
  .panel--front {
    left: 0;
    width: 413px;
  }
  .front__sky {
    position: absolute;
    inset: 0;
    background: linear-gradient(to bottom,
      var(--sky-top) 0%,
      var(--sky-mid) 32%,
      var(--sky-violet) 58%,
      var(--sky-orchid) 68%,
      var(--sky-blush) 84%,
      var(--hill-green) 92%,
      var(--hill-green) 100%);
  }
  .front__tagline {
    position: absolute;
    left: 0;
    width: 404px;
    top: 580px;
    margin: 0;
    text-align: center;
    font-size: 37px;
    font-weight: 500;
    line-height: 1;
  }
  .panel--info {
    left: 415px;
    width: 412px;
    background: var(--panel-lilac);
  }
  .panel--appointment {
    left: 829px;
    width: 371px;
    background: var(--panel-lilac);
  }
  .brand-name {
    position: absolute;
    left: 0;
    right: 0;
    margin: 0;
    text-align: center;
    font-size: 18.5px;
    font-weight: 500;
    letter-spacing: 0;
    line-height: 1;
    white-space: nowrap;
  }
  .panel--info .brand-name { top: 174px; }
  .panel--appointment .brand-name { top: 148px; left: 41px; }
  .rule-pair {
    position: absolute;
    overflow: visible;
  }
  .rule-pair ellipse { fill: var(--ink-brown); }
  .services {
    position: absolute;
    left: 0;
    right: 0;
    top: 457px;
    margin: 0;
    text-align: center;
    font-size: 26.5px;
    line-height: 41.5px;
  }
  .field-label {
    position: absolute;
    left: 41px;
    right: 0;
    margin: 0;
    text-align: center;
    font-size: 26px;
    line-height: 1;
  }
  .field-label--large { font-size: 29px; }
  .field-line {
    position: absolute;
    height: 2px;
    background: var(--ink-brown);
  }
  .date-blanks {
    position: absolute;
    left: 41px;
    right: 0;
    margin: 0;
    text-align: center;
    font-size: 26px;
    line-height: 1;
  }
  .date-blank {
    display: inline-block;
    height: 22px;
    border-bottom: 2px solid var(--ink-brown);
    vertical-align: bottom;
  }
  .date-blank--short { width: 38px; }
  .date-blank--long { width: 76px; }
  .date-slash { margin: 0 8px; }
</style>
</head>
<body>
<main class="card">

  <section class="panel panel--front">
    <div class="front__sky" role="img" aria-label="Illustration of a pastel sky with soft multicoloured clouds above rolling green hills"></div>
    <h2 class="front__tagline">Unique to your needs</h2>
  </section>

  <section class="panel panel--info">
    <h1 class="brand-name">MARIGOLD HOLLOW CLOTHING</h1>
    <svg class="rule-pair" style="left:80px; top:325px;" width="260" height="30" viewBox="0 0 260 30" aria-hidden="true">
      <ellipse cx="129" cy="3" rx="89" ry="1.8"/>
      <ellipse cx="128" cy="23" rx="127" ry="1.8"/>
    </svg>
    <p class="services">
      Design &amp; Manufacture of<br>
      clothing for those with<br>
      limited physical or cognitive<br>
      ability<br>
      at<br>
      47 Tallowmere Road<br>
      Wattlebrook, Qld, 4759
    </p>
  </section>

  <section class="panel panel--appointment">
    <h2 class="brand-name">MARIGOLD HOLLOW CLOTHING</h2>
    <svg class="rule-pair" style="left:80px; top:300px;" width="260" height="30" viewBox="0 0 260 30" aria-hidden="true">
      <ellipse cx="126" cy="3" rx="89" ry="1.8"/>
      <ellipse cx="126" cy="23" rx="125" ry="1.8"/>
    </svg>

    <p class="field-label" style="top:355px;">Name:</p>
    <div class="field-line" style="left:56px; width:300px; top:421px;"></div>

    <p class="field-label" style="top:479px;">Your next appointment is:</p>
    <p class="date-blanks" style="top:522px;">
      <span class="date-blank date-blank--short"></span><span class="date-slash">/</span><span class="date-blank date-blank--short"></span><span class="date-slash">/</span><span class="date-blank date-blank--long"></span>
    </p>

    <p class="field-label" style="top:604px;">At the time of:</p>
    <div class="field-line" style="left:119px; width:174px; top:671px;"></div>

    <p class="field-label field-label--large" style="top:724px;">To be held at:</p>
    <div class="field-line" style="left:48px; width:315px; top:799px;"></div>
    <div class="field-line" style="left:48px; width:315px; top:845px;"></div>
  </section>

</main>
</body>
</html>
```